Leading the way in online fitness and education requires power house web design

If you need to contact me you can do so via
skype: Drembal

We need a website designed for new company based in Houston Texas called "DrembalFit". We offer web based training and nutrition programs for our members for example we use the same software as these companies: http://marlowquist.com/ http://www.liftrova.com/ i would like my visitors to be captivated by the level of design creativity of the site.

colors to use would be grey, orange and green.
for example i like the green of this site http://www.cartiva.com/
i will upload my logo files so you can get a feel for shades of grey and orange.

there is a 3d effect filter i would like applied to my logo for use in the web design i have uploaded what that effect looks like.

i will need your designs to be complete with all interior pages which will include Home, Fitness, Nutrition, Fit Lounge, Fit Score, Fit School, Contact Us, Sign up.

fit lounge on my site is the same as pacebin on liftrova and locker room on marlowquist just re branded.

fit school is a research corner for members to learn about health and fitness, we are members of major medical journals on health and fitness and will have all our articles be from the newest research findings.

competitor sites
these sites use same software:
http://marlowquist.com/
http://www.liftrova.com/

these sites are other software.
http://home.stridelogix.com/software-for-athletes.aspx
http://www.vaultrix.com/

here are some websites that i like:
http://www.quorvamedia.com/
http://www.nib-forge.com/
http://velbun.com/
http://www.pralvix.com/
http://www.tormelix.de/fandoloo/
http://brewickstudio.com/

i also like the greens in this site that i am uploading
Updates

I have been reviewing the designs and would like to update everyone at once I do not want a normal fitness website design style, no testimonials, blog post, bodyfat calculator

my website will be a membership based website. i want the website to sell the main points of my fitness app that my members will have access to look at the comments for my selling points, use those points in the site create designs and graphics to visualize those points.

look at these sites and gain inspiration

http://www.dumelo.com.pl/#/projekty/case-studies
http://www.corvane.com/en#/home#ld-qpxn-604217-0039
http://www.nib-forge.com/
http://velbun.com/
http://www.pralvix.com/

i have a few designers asking me what the selling points are, the website needs to be built around these points

main selling points.

overview

programs utilize the best multi-joint exercises combined with high intensity cardio, to give you a full-body workout, efficiently and effectively. This means you’re burning more calories and building more lean muscle per unit of time than traditional weight training and cardio programs.

When you sign up, you''ll receive a work out and diet plan to fit your goals and fitness level. As you progress through your plan, you can use the personal fitness and meal calendar to record your results. When you sign-up we''ll ask you a series of questions and your workouts will be tailored to your exact needs. That means never having to use a generic diet and exercise plan again.

If you''ve ever tried to lose weight and build muscle and didn''t succeed, we feel your pain. Until now, trying to navigate all the fitness fads and latest trends on your own has been difficult. The best option - hiring a certified personal trainer - may be out of your financial reach. That''s where we come in - we''re personal trainers on a mission to help you reach your fitness goals quickly and for less money than in person training. Best of all, we''re here to help you day or night.

Fitness

Personal Fitness Calendar

Tailored to the member’s schedule and flexible to accommodate any changes to a member’s regular fitness schedule. Track your progress and stay on track with your fitness goals.

Custom Fitness Plan

Based on a member’s current physical condition and goals.

• Step by step exercise instructions
• 3-D video demonstrations of over 600 exercises, including functional and body-weight only movements
• Equipment filter can customize plans to your gym’s equipment package
• Record workouts to track exercise history and progression

Nutrition

Nutritional Assessment

Daily recommended caloric intake (Protein, Carbohydrates and Fats), based on personal profile and daily fitness plan.

Custom Meal Plan

Personalized meal plan based on nutritional assessment.

• Choose number of meals per day
• Add dietary restrictions, food preferences or dislikes
• Database of thousands of ingredients allows for hundreds of thousands of meal combinations
• Include favorite foods by entering custom nutritional information

Weight tracking

Calculate goal weight and track weight-loss or weight-gain progress. You will reach your goals in no time.

Fit Lounge

What is the most important part of any workout or fitness program? Staying motivated. And what better form of motivation than positive encouragement from your peers?

Fit Lounge is fitness focused social network for health-minded individuals looking for a simple and convenient place to track their workout goals and monitor their progress. A unique system of motivation, support and accountability makes setting fitness goals and then keeping up with them easy

Track

Start by setting fitness goals that you want to track. They can be anything from running and jogging to how many hours of sleep you are getting and how many glasses of water you are drinking every day. Other members of the drembalfits community might be tracking the same workout goals as you, so you can always join their groups as well.

Share

Once you start tracking your workout goals, you can share your progress with your friends. Reach a new max on your bench press? Let everyone know. Eclipse the 10 mile mark on your daily run? Spread the word! The communication of encouragement back and forth is a great way to ensure that everyone stays on track with their workout goals.

Achieve

Of course, the point of any workout or fitness program is to achieve the goals you’ve set. And with help from drembalfits workout tracking tools and encouragement from the community, you will achieve your workout goals in no time. When you see a friend has achieved his or her fitness goals, you can send them a virtual “fist bump” as a sign of congratulations. The number of “fist bumps” each user accumulates will be displayed on their profile, providing additional motivation and a healthy dose of competition.

Reason: i dont feel the designs i have received are of the quality i am looking for

check this website out, i know its flash, but i also know you can get creative without flash and have nice effects throughout the site.

http://www.lanterfold-hub.com/

I dont want plain jane designs, insert the content i provided into the site and have it explored in a unique way. take as much time on the design as you need as i will keep extending deadline until i find one that is perfect.

as said before don't make the site anything like the competition sites, its only purpose is to sell the memberships using content provided so i need an innovative way to for them to explore that content,

as your designing this site add me on skype so i can detail and help brainstorm ideas my skype id is drembal
you can stray from the color scheme a little or throw it away if you want i just want to see how creative you can get.

Industry/Entity Type

School

Requirements
Nice to have
• if you notice at the bottom of http://marlowquist.com/ she has the orange bar with the three short content parts, i like the idea of having a space like that for similar content.

on http://www.vaultrix.com/ if you look to the left side of the scrolling icons i like the idea of having icons or animated pictures to point of key benefits.

```html
<!DOCTYPE html>
<html lang="en">
<head>
<meta charset="utf-8">
<title>DrembalFit</title>
<link rel="stylesheet" href="https://fonts.googleapis.com/css2?family=Arvo:wght@400;700&family=Bebas+Neue&display=swap">
<style>
:root{
  --ink:#2b2b2b;
  --text:#555;
  --bar:#333;
  --bar-dark:#222;
  --orange:#e8681a;
  --orange-light:#f58a2c;
  --panel:#ececec;
  --panel-line:#dedede;
  --white:#fff;
  --tick:#5a9a2e;
}
*{box-sizing:border-box;margin:0;padding:0}
html,body{width:693px;height:1200px;overflow:hidden}
body{position:relative;background:var(--white);font-family:"Arvo",serif;color:var(--text);font-size:10px;line-height:1.45}
.abs{position:absolute}
a{color:inherit;text-decoration:none}

.topbar{left:0;top:0;width:693px;height:22px;background:var(--bar-dark);border-bottom:2px solid #111}
.topbar .links{right:8px;top:4px;color:#ddd;font-size:9.5px;word-spacing:2px;white-space:nowrap}
.header{left:0;top:22px;width:693px;height:425px;background:linear-gradient(#e6e6e6,#f3f3f3 40%,#d8d8d8)}
.logo{left:22px;top:58px;display:flex;align-items:center;gap:6px;font-weight:700;font-size:19px;color:#3a3a3a;white-space:nowrap}
.logo .dot{width:11px;height:11px;border-radius:50%;background:var(--orange)}
.subscribe{left:510px;top:34px;width:136px;height:27px;background:var(--white);border:1px solid #ccc;border-radius:3px;font-size:8px;color:#aaa;font-style:italic;padding:7px 10px;white-space:nowrap}
.go{left:650px;top:34px;width:36px;height:27px;background:#3a3a3a;border-radius:3px;color:#fff;font-size:10.5px;text-align:center;line-height:27px}
.nav{left:222px;top:72px;display:flex;font-size:9.6px;color:var(--ink);white-space:nowrap}
.nav a{padding:4px 6px;line-height:14px}
.nav a.active{background:var(--orange);color:#fff;border-radius:2px;padding:4px 9px}

.hero-photo{left:14px;top:133px;width:665px;height:254px;border-radius:0 0 332px 332px/0 0 36px 36px;background:linear-gradient(#e4e4e4,#cdd3c8)}
.arrow{top:180px;width:14px;height:50px}
.bubble{left:394px;top:133px;width:254px;height:156px;background:var(--white);border-radius:14px;box-shadow:0 2px 6px rgba(0,0,0,.15);padding:14px 14px}
.bubble h1{font-family:"Bebas Neue",sans-serif;font-weight:400;color:var(--ink);font-size:21px;line-height:22px;white-space:nowrap}
.bubble h2{font-family:"Bebas Neue",sans-serif;font-weight:400;color:var(--ink);font-size:25px;line-height:27px;margin-bottom:6px;white-space:nowrap}
.bubble p{font-size:8.8px;line-height:1.45;color:#333}
.bubble-tail{left:470px;top:286px}

.strip{left:13px;top:400px;width:671px;height:80px;background:var(--white);box-shadow:0 1px 3px rgba(0,0,0,.2)}
.strip-inner{left:10px;top:9px;width:651px;height:62px;display:flex;gap:2px}
.thumb{flex:1;background:#3a3a3a;display:flex;gap:6px;padding:8px 6px;color:#fff;font-size:8.5px;line-height:1.3;overflow:hidden}
.thumb.current{background:#6a6a6a}
.thumb .pic{width:42px;height:40px;flex:none;background:linear-gradient(#dfe6ea,#9fb3c0)}
.strip-notch{left:332px;top:392px}

.cta{left:9px;top:490px;width:675px;height:46px;background:linear-gradient(var(--orange-light),var(--orange));color:#fff;font-size:12.5px;white-space:nowrap}
.cta .lead{left:16px;top:14px}
.cta .pitch{left:146px;top:14px}
.cta .sep{left:122px;top:0}
.cta .btn{left:522px;top:9px;width:138px;height:28px;background:#333;border-radius:3px;text-align:center;line-height:28px;font-size:11px}

.section-head{height:29px;background:var(--panel);color:var(--ink);font-size:12.5px;padding:7px 8px;white-space:nowrap}
.believe-head{left:9px;top:549px;width:675px}
.believe{left:16px;top:586px;width:664px;font-size:9px;line-height:1.5}

.members-head{left:9px;top:696px;width:484px}
.member{width:240px;height:64px;display:flex;gap:10px}
.member .pic{width:56px;height:56px;flex:none;border:1px solid #ddd;background:linear-gradient(#f0ebe6,#c8b4a2)}
.member h3{font-size:10px;color:var(--ink);font-weight:700;margin-bottom:2px;white-space:nowrap}
.member p{font-size:9px;line-height:1.4}

.benefits{left:515px;top:696px;width:168px;height:273px;background:var(--panel)}
.benefits .section-head{background:#e4e4e4}
.benefit-list{left:10px;top:42px;width:150px;list-style:none}
.benefit-list li{display:flex;align-items:center;gap:7px;height:26px;font-size:9.2px;color:#444;white-space:nowrap}
.benefit-list svg{flex:none}
.benefits .btn{left:16px;top:226px;width:137px;height:28px;border-radius:3px;background:linear-gradient(#555,#2e2e2e);color:#fff;text-align:center;line-height:28px;font-size:11px}

.features{left:0;top:989px;width:693px;height:155px;background:var(--panel);display:flex}
.feature{flex:1;padding:18px 16px;border-right:1px solid var(--panel-line);font-size:9px;line-height:1.5}
.feature:last-child{border:none}
.feature h3{font-size:12px;font-weight:400;color:var(--ink);margin-bottom:10px}

.footer{left:0;top:1144px;width:693px;height:56px;background:var(--bar)}
.footer .nav-links{left:10px;top:13px;color:#ddd;font-size:9.5px;display:flex;gap:18px;white-space:nowrap}
.footer .copy{left:10px;top:34px;color:#bbb;font-size:8px}
.social{right:12px;top:16px;display:flex;gap:5px}
.social span{width:23px;height:23px;border-radius:3px}
</style>
</head>
<body>

<div class="topbar abs"><div class="links abs"><a>Signup</a> | <a>Login</a> | <a>Shopping cart (0)</a></div></div>

<div class="header abs"></div>
<div class="logo abs"><span class="dot"></span>DrembalFit</div>
<div class="subscribe abs">subscribe to newsletter</div>
<div class="go abs">Go</div>
<nav class="nav abs">
  <a class="active">Home</a><a>Fitness</a><a>Nutrition</a><a>Fit Lounge</a><a>Fit Score</a><a>Fit School</a><a>Signup</a><a>Contact Us</a>
</nav>

<div class="hero-photo abs" role="img" aria-label="Photo of a woman doing a crunch on a round grass platform"></div>
<svg class="arrow abs" style="left:6px" viewBox="0 0 14 50"><polyline points="12,2 2,25 12,48" fill="none" stroke="#bbb" stroke-width="2"/></svg>
<svg class="arrow abs" style="left:673px" viewBox="0 0 14 50"><polyline points="2,2 12,25 2,48" fill="none" stroke="#bbb" stroke-width="2"/></svg>

<div class="bubble abs">
  <h1>Your personal trainer online</h1>
  <h2>Day or night, for less.</h2>
  <p>Multi-joint exercises combined with high intensity cardio give you a full-body workout, burning more calories and building more lean muscle per unit of time.</p>
</div>
<svg class="bubble-tail abs" width="30" height="24" viewBox="0 0 30 24"><polygon points="0,0 28,0 6,22" fill="#fff"/></svg>

<div class="strip abs">
  <div class="strip-inner abs">
    <div class="thumb"><div class="pic" role="img" aria-label="Photo of a woman in fitness gear"></div><div>Personal fitness calendar</div></div>
    <div class="thumb"><div class="pic" role="img" aria-label="Photo of a woman stretching outdoors"></div><div>Custom plan for your goals</div></div>
    <div class="thumb current"><div class="pic" role="img" aria-label="Photo of a man lifting weights"></div><div>3-D demos of 600 exercises</div></div>
    <div class="thumb"><div class="pic" role="img" aria-label="Photo of a woman in a yoga pose"></div><div>Custom meal plan</div></div>
    <div class="thumb"><div class="pic" role="img" aria-label="Photo of a woman stretching on a mat"></div><div>Fit Lounge community</div></div>
  </div>
</div>
<svg class="strip-notch abs" width="24" height="9" viewBox="0 0 24 9"><polygon points="0,9 12,0 24,9" fill="#fff"/></svg>

<div class="cta abs">
  <div class="lead abs">Ready to get fit ?</div>
  <svg class="sep abs" width="16" height="46" viewBox="0 0 16 46"><polyline points="2,0 14,23 2,46" fill="none" stroke="#ffb06b" stroke-width="1.5"/></svg>
  <div class="pitch abs">Let drembal fit help you get in the best shape of your life</div>
  <div class="btn abs">Get Started</div>
</div>

<div class="section-head believe-head abs">What we believe</div>
<p class="believe abs">If you've ever tried to lose weight and build muscle and didn't succeed, we feel your pain. Until now, trying to navigate all the fitness fads and latest trends on your own has been difficult. The best option, hiring a certified personal trainer, may be out of your financial reach. That's where we come in: we're personal trainers on a mission to help you reach your fitness goals quickly and for less money than in person training. When you sign up, we'll ask you a series of questions and you'll receive a workout and diet plan tailored to your goals and fitness level. As you progress, use the personal fitness and meal calendar to record your results. That means never having to use a generic diet and exercise plan again. Best of all, we're here to help you day or night.</p>

<div class="section-head members-head abs">Latest members</div>
<div class="member abs" style="left:16px;top:736px"><div class="pic" role="img" aria-label="Member portrait"></div><div><h3>Track</h3><p>Set goals, from your daily run to glasses of water, and join groups tracking the same.</p></div></div>
<div class="member abs" style="left:267px;top:736px"><div class="pic" role="img" aria-label="Member portrait"></div><div><h3>Share</h3><p>Reach a new max on your bench press? Let all your friends in the Fit Lounge know.</p></div></div>
<div class="member abs" style="left:16px;top:820px"><div class="pic" role="img" aria-label="Member portrait"></div><div><h3>Achieve</h3><p>Reach your goals with workout tracking tools and the support of the community.</p></div></div>
<div class="member abs" style="left:267px;top:820px"><div class="pic" role="img" aria-label="Member portrait"></div><div><h3>Fist bumps</h3><p>Congratulate a friend on a goal; every fist bump shows up on their profile.</p></div></div>
<div class="member abs" style="left:16px;top:901px"><div class="pic" role="img" aria-label="Member portrait"></div><div><h3>Stay motivated</h3><p>Positive encouragement from your peers keeps you on track, week after week.</p></div></div>
<div class="member abs" style="left:267px;top:901px"><div class="pic" role="img" aria-label="Member portrait"></div><div><h3>Weight tracking</h3><p>Calculate a goal weight and follow your weight-loss or weight-gain progress.</p></div></div>

<div class="benefits abs">
  <div class="section-head">Member benefits</div>
  <ul class="benefit-list abs">
    <li><svg width="12" height="12" viewBox="0 0 12 12"><polyline points="1.5,6.5 4.5,9.5 10.5,2.5" fill="none" stroke="var(--tick)" stroke-width="2"/></svg>Fitness calendar</li>
    <li><svg width="12" height="12" viewBox="0 0 12 12"><polyline points="1.5,6.5 4.5,9.5 10.5,2.5" fill="none" stroke="var(--tick)" stroke-width="2"/></svg>Custom fitness plan</li>
    <li><svg width="12" height="12" viewBox="0 0 12 12"><polyline points="1.5,6.5 4.5,9.5 10.5,2.5" fill="none" stroke="var(--tick)" stroke-width="2"/></svg>Equipment filter</li>
    <li><svg width="12" height="12" viewBox="0 0 12 12"><polyline points="1.5,6.5 4.5,9.5 10.5,2.5" fill="none" stroke="var(--tick)" stroke-width="2"/></svg>Nutritional assessment</li>
    <li><svg width="12" height="12" viewBox="0 0 12 12"><polyline points="1.5,6.5 4.5,9.5 10.5,2.5" fill="none" stroke="var(--tick)" stroke-width="2"/></svg>Custom meal plan</li>
    <li><svg width="12" height="12" viewBox="0 0 12 12"><polyline points="1.5,6.5 4.5,9.5 10.5,2.5" fill="none" stroke="var(--tick)" stroke-width="2"/></svg>Weight tracking</li>
    <li><svg width="12" height="12" viewBox="0 0 12 12"><polyline points="1.5,6.5 4.5,9.5 10.5,2.5" fill="none" stroke="var(--tick)" stroke-width="2"/></svg>Fit Lounge access</li>
  </ul>
  <div class="btn abs">Sign up</div>
</div>

<div class="features abs">
  <div class="feature"><h3>Slim down</h3>Daily recommended caloric intake of protein, carbohydrates and fats, based on your personal profile and daily plan. Choose the number of meals per day and add dietary restrictions, food preferences or dislikes.</div>
  <div class="feature"><h3>Get fit</h3>A custom fitness plan based on your current condition and goals, with step by step instructions and 3-D video demonstrations of over 600 exercises. Record workouts to track your history and progression.</div>
  <div class="feature"><h3>Be sexy</h3>A calendar tailored to your schedule and flexible to any changes. Track your progress, share it with friends in the Fit Lounge and collect fist bumps as you reach your goals in no time.</div>
</div>

<div class="footer abs">
  <div class="nav-links abs"><a>Home</a><a>Fitness</a><a>Nutrition</a><a>Fit Lounge</a><a>Fit Score</a><a>Fit School</a><a>Signup</a><a>Contact Us</a></div>
  <div class="copy abs">© 2012 Drembalfit.com. All Rights Reserved.</div>
  <div class="social abs">
    <span style="background:#3b5a9a"></span>
    <span style="background:#3fa9e0"></span>
    <span style="background:#f08a1c"></span>
    <span style="background:#c4302b"></span>
  </div>
</div>

</body>
</html>
```